New Signage Design Project

Real estate company looking for signage, PowerPoint and stationery branding. Signs will be placed in front of homes and other properties being sold

Name of company is Tern Haven, LLC

Requirements
Must have
• Name of company - Tern Haven, LLC

```html
<!DOCTYPE html>
<html lang="en">
<head>
<meta charset="utf-8">
<title>Tern Haven, LLC – Sold Yard Sign</title>
<link rel="stylesheet" href="https://fonts.googleapis.com/css2?family=Montserrat:wght@500;600;700;800&display=swap">
<style>
  :root {
    --page: #eef0f0;
    --charcoal: #232b2c;
    --coral: #e2505c;
    --white: #ffffff;
    --shirt-light: #dfe9f2;
    --shirt-mid: #b9c8d6;
  }
  html, body {
    margin: 0;
    padding: 0;
    width: 966px;
    height: 1200px;
    overflow: hidden;
    background: var(--page);
  }
  .canvas {
    position: relative;
    width: 966px;
    height: 1200px;
  }
  .yard-sign {
    position: absolute;
    left: 30px;
    top: 238px;
    width: 906px;
    height: 724px;
    display: block;
    box-shadow: 0 10px 30px rgba(0,0,0,0.18);
  }
  .sign-text { font-family: "Montserrat", sans-serif; }
  .headline { font-weight: 800; fill: var(--white); }
  .company-name { font-weight: 700; fill: var(--white); letter-spacing: 1px; }
  .agent-name { font-weight: 500; fill: var(--white); }
  .phone-number { font-weight: 700; fill: var(--white); }
  .web-address { font-weight: 500; fill: var(--white); }
</style>
</head>
<body>
<main class="canvas">
  <svg class="yard-sign" viewBox="0 0 1069 854" xmlns="http://www.w3.org/2000/svg">
    <defs>
      <linearGradient id="agentPhotoTone" x1="0" y1="0" x2="1" y2="1">
        <stop offset="0" stop-color="var(--shirt-light)"/>
        <stop offset="1" stop-color="var(--shirt-mid)"/>
      </linearGradient>
    </defs>

    <!-- panel background -->
    <rect class="panel-lower" x="0" y="0" width="1069" height="854" fill="var(--coral)"/>
    <path class="swoosh" d="M22,310 C300,559 750,559 1069,375 V290 C750,518 300,515 22,310 Z" fill="var(--white)"/>
    <path class="panel-upper" d="M0,0 H1069 V280 C700,507 300,507 0,280 Z" fill="var(--charcoal)"/>

    <!-- headline -->
    <text class="sign-text headline" x="535" y="240" font-size="258" text-anchor="middle" textLength="750" lengthAdjust="spacingAndGlyphs">SOLD</text>

    <!-- company -->
    <circle class="company-dot" cx="535" cy="330" r="38" fill="var(--coral)"/>
    <text class="sign-text company-name" x="535" y="422" font-size="25" text-anchor="middle">TERN HAVEN, LLC</text>

    <!-- agent photo area -->
    <path class="agent-photo" role="img" aria-label="Portrait photo of the agent, smiling with arms crossed, wearing a light blue shirt"
          d="M830,252 C900,240 960,270 960,340 C960,390 950,420 960,440 C1020,470 1062,520 1062,600 V854 H745 V760 C700,740 675,720 680,690 C690,640 700,580 730,540 C770,500 810,490 840,470 C820,430 815,380 815,330 C815,290 820,260 830,252 Z"
          fill="url(#agentPhotoTone)"/>

    <!-- agent name -->
    <text class="sign-text agent-name" x="80" y="612" font-size="92">ADA WREN</text>

    <!-- phone -->
    <rect class="phone-pill" x="140" y="643" width="570" height="87" rx="43.5" fill="var(--charcoal)"/>
    <circle class="phone-badge" cx="127" cy="688" r="44" fill="var(--white)" stroke="var(--coral)" stroke-width="4"/>
    <g class="phone-icon" transform="translate(107 668)" fill="none" stroke="var(--coral)" stroke-width="3" stroke-linecap="round" stroke-linejoin="round">
      <path d="M8,4 L15,4 L18,13 L13,17 C15,23 19,27 25,29 L29,24 L38,27 L38,34 C38,37 35,39 32,39 C17,38 4,25 3,10 C3,7 5,4 8,4 Z"/>
      <path d="M24,10 C29,11 32,14 33,19"/>
      <path d="M24,3 C33,4 39,10 40,19"/>
    </g>
    <text class="sign-text phone-number" x="192" y="715" font-size="70" textLength="478" lengthAdjust="spacingAndGlyphs">0198 765 432</text>

    <!-- web and badges -->
    <g class="globe-icon" fill="none" stroke="var(--white)" stroke-width="2.2">
      <circle cx="93" cy="788" r="13"/>
      <ellipse cx="93" cy="788" rx="6" ry="13"/>
      <line x1="80" y1="788" x2="106" y2="788"/>
      <line x1="82" y1="781" x2="104" y2="781"/>
      <line x1="82" y1="795" x2="104" y2="795"/>
    </g>
    <text class="sign-text web-address" x="118" y="798" font-size="33">www.ternhaven.com</text>
    <line class="divider" x1="499" y1="772" x2="499" y2="804" stroke="var(--white)" stroke-width="2"/>
    <rect class="badge" x="527" y="766" width="42" height="34" rx="3" fill="var(--white)"/>
    <rect class="badge" x="580" y="766" width="32" height="34" rx="3" fill="var(--white)"/>
  </svg>
</main>
</body>
</html>
```